Design a New Business Card for Our Company

We are looking for fresh, unique, and a modern business card that reflects our roots as digital marketing agency focused on SEM.

Industry/Entity Type

Marketing

Contact Information for Business Card

looking for very unique out of the box designs. clean and modern that compliments our logo

Requirements
Must have
• colors should match our logo
• Front should have name, address, email, and phone/fax of the person, phone/fax are the same number
• back should have our url

```html
<!DOCTYPE html>
<html lang="en">
<head>
<meta charset="utf-8">
<title>Quorvane Solutions – Business Card</title>
<link href="https://fonts.googleapis.com/css2?family=Lato:wght@400;700&display=swap" rel="stylesheet">
<style>
  :root {
    --stage: #000000;
    --card-front: #f2f2f2;
    --brand-blue: #5a93d2;
    --brand-grey: #a6a6a6;
    --text-dark: #2e2e2e;
    --back-top: #9e9e9e;
    --back-bottom: #bcbcbc;
    --white: #ffffff;
  }
  * { margin: 0; padding: 0; box-sizing: border-box; }
  html, body { width: 1200px; height: 900px; overflow: hidden; background: var(--stage); }
  body { position: relative; font-family: "Lato", Arial, sans-serif; }

  .card { position: absolute; top: 200px; width: 310px; height: 502px; overflow: hidden; }
  .card-front { left: 265px; background: var(--card-front); border-radius: 62px 0 62px 0; }
  .card-back { left: 641px; width: 309px; border-radius: 0 62px 0 62px; }

  .brand-dot { position: absolute; left: 139px; top: 40px; width: 72px; height: 72px; border-radius: 50%; background: var(--brand-blue); }

  .wordmark { position: absolute; left: 0; width: 100%; text-align: center; font-weight: 700; line-height: 1; white-space: nowrap; }
  .front-wordmark { top: 154px; color: var(--brand-grey); padding-left: 42px; }
  .wordmark-name { display: block; font-size: 50px; letter-spacing: -1.5px; }
  .wordmark-tag { display: block; font-size: 14px; letter-spacing: 10.5px; margin-top: 4px; padding-left: 10px; }

  .person { position: absolute; left: 24px; top: 298px; }
  .person-name { font-size: 19px; font-weight: 700; color: var(--brand-blue); line-height: 1.2; }
  .person-role { font-size: 14px; color: var(--text-dark); line-height: 1.3; }

  .address { position: absolute; left: 23px; top: 361px; font-size: 14px; color: var(--text-dark); line-height: 15px; font-style: normal; }

  .contacts { position: absolute; left: 24px; top: 411px; list-style: none; font-size: 14px; color: var(--text-dark); }
  .contacts li { display: flex; align-items: center; height: 20.5px; white-space: nowrap; }
  .contacts svg { width: 10px; height: 10px; margin-right: 6px; fill: var(--brand-blue); flex: none; }

  .back-texture { position: absolute; inset: 0; background: linear-gradient(180deg, var(--back-top), var(--back-bottom)); }
  .back-wordmark { top: 333px; color: var(--white); }
  .back-wordmark .wordmark-name { font-size: 54px; }
  .back-wordmark .wordmark-tag { font-size: 15px; letter-spacing: 11px; margin-top: 2px; }
  .website { position: absolute; left: 0; width: 100%; top: 420px; text-align: center; color: var(--white); font-size: 18px; font-weight: 700; white-space: nowrap; }
</style>
</head>
<body>

  <section class="card card-front" aria-label="Business card front">
    <span class="brand-dot"></span>
    <div class="wordmark front-wordmark">
      <span class="wordmark-name">quorvane</span>
      <span class="wordmark-tag">SOLUTIONS</span>
    </div>

    <div class="person">
      <p class="person-name">Daniel Moore</p>
      <p class="person-role">Managing Director</p>
    </div>

    <address class="address">2417, Maple Street West<br>Northland, 204518</address>

    <ul class="contacts">
      <li>
        <svg viewBox="0 0 10 10" aria-hidden="true"><path d="M2 0.5 L3.6 2.6 L2.7 3.6 Q3.6 5.7 6.4 7.3 L7.4 6.4 L9.5 8 L8.4 9.5 Q2 8.5 0.5 1.6 Z"/></svg>
        (044)-555-0148
      </li>
      <li>
        <svg viewBox="0 0 10 10" aria-hidden="true"><path d="M2.5 0.5 H7 V3 H9.5 V9.5 H0.5 V3 H2.5 Z M3.5 1.5 V3 H6 V1.5 Z M2 5 V6 H4 V5 Z M5 5 V6 H8 V5 Z M2 7 V8 H4 V7 Z M5 7 V8 H8 V7 Z" fill-rule="evenodd"/></svg>
        123-555-0190
      </li>
      <li>
        <svg viewBox="0 0 10 10" aria-hidden="true"><path d="M0.5 2 H9.5 V8.5 H0.5 Z"/><path d="M1.2 2.6 L5 5.6 L8.8 2.6" stroke="#f2f2f2" stroke-width="0.8" fill="none"/></svg>
        hello@quorvane-example.com
      </li>
    </ul>
  </section>

  <section class="card card-back" aria-label="Business card back">
    <div class="back-texture" role="img" aria-label="Grey background scattered with soft round bubble shapes"></div>
    <div class="wordmark back-wordmark">
      <span class="wordmark-name">quorvane</span>
      <span class="wordmark-tag">SOLUTIONS</span>
    </div>
    <p class="website">www.quorvane-example.com</p>
  </section>

</body>
</html>
```